The Timber Loft

We need a business card design for our wardrobe company.
Please visit our website www.zorvelcabinets.com to get an idea of who we are.

```html
<!DOCTYPE html>
<html lang="en">
<head>
<meta charset="utf-8">
<title>The Timber Loft – Business Card</title>
<link rel="stylesheet" href="https://fonts.googleapis.com/css2?family=Roboto:wght@400;500&display=swap">
<style>
  :root {
    --page-bg: #9a9a9a;
    --card-dark: #1f1d1c;
    --card-dark-2: #36322f;
    --card-dark-3: #4a4643;
    --paper: #ffffff;
    --ink: #111111;
    --ink-light: #f4f4f4;
    --ink-muted: #d6d6d6;
    --rim: #b9b9b9;
  }
  * { box-sizing: border-box; margin: 0; padding: 0; }
  html, body {
    width: 1200px; height: 930px; overflow: hidden;
    background: var(--page-bg);
    font-family: "Roboto", Arial, sans-serif;
  }
  .canvas { position: relative; width: 1200px; height: 930px; }
  .card {
    position: absolute; left: 220px;
    width: 760px; height: 420px;
    border-radius: 34px; overflow: hidden;
    box-shadow: 0 14px 30px rgba(0,0,0,.35);
  }
  .card--front { top: 35px; }
  .card--back { top: 475px; }

  .card__photo {
    position: absolute; inset: 0;
    background: linear-gradient(180deg, var(--card-dark-3) 0%, var(--card-dark-2) 22%, var(--card-dark) 60%, #151413 100%);
  }
  .card__photo::after {
    content: ""; position: absolute; inset: 0;
    background: radial-gradient(ellipse at 60% 55%, rgba(120,110,100,.22), transparent 65%);
  }

  .brand { position: absolute; display: flex; align-items: center; gap: 16px; }
  .brand__square { width: 74px; height: 54px; border: 3px solid currentColor; flex: none; }
  .brand__name {
    font-size: 22px; font-weight: 500; letter-spacing: .5px; text-transform: uppercase; line-height: 1.3;
  }
  .brand__tagline { font-size: 19px; font-weight: 400; }
  .card--front .brand { left: 210px; top: 178px; color: var(--ink-light); }

  .disc { position: absolute; inset: 0; }
  .card--back .brand { left: 445px; top: 176px; color: var(--ink); }
  .card--back .brand__square { width: 64px; height: 46px; }
  .card--back .brand__name { font-size: 19px; }
  .card--back .brand__tagline { font-size: 16px; }

  .contact { position: absolute; left: 48px; top: 150px; color: var(--ink-light); }
  .contact__name {
    font-size: 31px; font-weight: 500; letter-spacing: 1px; text-transform: uppercase;
  }
  .contact__role { font-size: 17px; color: var(--ink-muted); margin: 2px 0 0 22px; }
  .contact__address {
    font-size: 19px; color: var(--ink-muted); margin: 24px 0 0 48px; line-height: 1.35;
  }
  .contact__list { list-style: none; margin: 18px 0 0 48px; font-size: 19px; color: var(--ink-muted); }
  .contact__list li { display: flex; align-items: center; gap: 12px; line-height: 1.45; }
  .contact__list svg { width: 16px; height: 16px; fill: none; stroke: var(--ink-muted); stroke-width: 1.8; }
</style>
</head>
<body>
<main class="canvas">

  <section class="card card--front">
    <div class="card__photo" role="img" aria-label="Dimly lit walk-in wardrobe with open shelving and hanging clothes"></div>
    <div class="brand">
      <span class="brand__square"></span>
      <div>
        <p class="brand__name">The Timber Loft</p>
        <p class="brand__tagline">Crafted to fit your space</p>
      </div>
    </div>
  </section>

  <section class="card card--back">
    <div class="card__photo" role="img" aria-label="Dimly lit walk-in wardrobe with open shelving and hanging clothes"></div>
    <svg class="disc" viewBox="0 0 760 420" aria-hidden="true">
      <circle cx="640" cy="190" r="300" fill="var(--rim)"/>
      <circle cx="660" cy="180" r="296" fill="var(--paper)"/>
    </svg>
    <div class="contact">
      <h1 class="contact__name">Daniel Hartley</h1>
      <p class="contact__role">Director</p>
      <p class="contact__address">Larch Court, 42 Mill Lane,<br>London N4 7QT</p>
      <ul class="contact__list">
        <li>
          <svg viewBox="0 0 16 16"><path d="M3 1.5h3l1.2 3.2-1.8 1.2a8 8 0 0 0 4.7 4.7l1.2-1.8 3.2 1.2v3a1.5 1.5 0 0 1-1.6 1.5A13 13 0 0 1 1.5 3.1 1.5 1.5 0 0 1 3 1.5z"/></svg>
          0207 555 0184
        </li>
        <li>
          <svg viewBox="0 0 16 16"><rect x="1.5" y="3" width="13" height="10" rx="1"/><path d="M1.5 3.5 8 9l6.5-5.5"/></svg>
          info@zorvelcabinets.com
        </li>
        <li>
          <svg viewBox="0 0 16 16"><circle cx="8" cy="8" r="6.5"/><path d="M1.5 8h13M8 1.5c-2.5 3.5-2.5 9.5 0 13M8 1.5c2.5 3.5 2.5 9.5 0 13"/></svg>
          www.zorvelcabinets.com
        </li>
      </ul>
    </div>
    <div class="brand">
      <span class="brand__square"></span>
      <div>
        <p class="brand__name">The Timber Loft</p>
        <p class="brand__tagline">Crafted to fit your space</p>
      </div>
    </div>
  </section>

</main>
</body>
</html>
```